Vacation giveaway landing page design

We are giving away a holiday/vacation to Rome and we need a landing page designed that will entice people to enter their email address for a chance to win!

Full brief, examples and everything else can be found in this document: https://files.quorvanshare.net/page/7-tmzrwpQY4vxkaLn8sbgeXu2fcTo5kWdn3jhpyuBc29m/open?mode=viewing

Number of Pages Required

1 page

```html
<!DOCTYPE html>
<html lang="en">
<head>
<meta charset="UTF-8">
<title>Join &amp; Win a Holiday in Rome</title>
<link rel="stylesheet" href="https://fonts.googleapis.com/css2?family=Fredoka:wght@500;600;700&family=Open+Sans:wght@400;600;700&display=swap">
<style>
:root{
  --yellow:#ffd42e;
  --yellow-deep:#ffbe12;
  --navy:#2c3d52;
  --cyan:#1ea3e2;
  --red:#ef5b4b;
  --card:#fff6c4;
  --card-top:#ffe87a;
  --tick:#2fb8a6;
  --grey-bg:#f1f1f1;
  --footer:#2e5664;
  --text:#3b4a5c;
  --white:#ffffff;
}
*{box-sizing:border-box;margin:0;padding:0}
html,body{width:1200px;height:2632px;overflow:hidden}
body{position:relative;background:var(--white);font-family:"Open Sans",Arial,sans-serif;color:var(--text)}

/* Hero */
.hero{position:absolute;left:0;top:0;width:1200px;height:860px;background:linear-gradient(180deg,var(--yellow) 0%,var(--yellow-deep) 100%);overflow:hidden}
.brand{position:absolute;left:0;width:1200px;top:28px;text-align:center}
.brand-dot{display:block;margin:0 auto 10px;width:44px;height:44px;border-radius:50%;background:var(--navy)}
.brand-name{font-family:"Fredoka",Arial,sans-serif;font-weight:700;font-size:28px;letter-spacing:2px;color:var(--navy);text-transform:uppercase}
.headline{position:absolute;left:0;width:1200px;top:184px;text-align:center;color:var(--white);font-family:"Fredoka",Arial,sans-serif;font-weight:700;text-transform:uppercase;line-height:1}
.headline .l1{font-size:66px;display:block}
.headline .l2{font-size:40px;display:block;margin-top:6px}
.headline .l3{font-size:40px;display:block;margin-top:2px}
.headline .l3 b{font-size:72px;color:var(--navy);vertical-align:-4px}
.headline .l4{font-size:40px;display:block;margin-top:2px}
.rule{position:absolute;top:218px;height:3px;width:140px;background:var(--white)}
.signup{position:absolute;left:112px;top:440px;width:310px}
.field{display:block;width:310px;height:40px;margin-bottom:16px;border-radius:20px;background:var(--white);padding:0 18px;font-size:14px;line-height:40px;color:#8a94a0}
.field.select{position:relative}
.field.select::after{content:"";position:absolute;right:18px;top:16px;border:6px solid transparent;border-top-color:var(--cyan)}
.consent{display:flex;gap:12px;margin-top:6px;font-size:11.5px;line-height:1.45;color:var(--navy)}
.consent .box{flex:0 0 18px;height:18px;border-radius:4px;background:var(--white);margin-top:2px}
.btn{display:inline-block;background:var(--cyan);color:var(--white);border-radius:24px;font-weight:700;text-align:center}
.signup .btn{margin-top:30px;width:140px;height:44px;line-height:44px;font-size:14px}
.island-art{position:absolute;left:560px;top:480px;width:640px;height:380px;background:linear-gradient(180deg,rgba(255,255,255,0) 0%,rgba(255,255,255,.35) 55%,var(--white) 88%)}

/* Join */
.section-title{position:absolute;left:0;width:1200px;text-align:center;font-family:"Fredoka",Arial,sans-serif;font-weight:600;font-size:34px;letter-spacing:2px;color:var(--navy);text-transform:uppercase}
.section-title::before,.section-title::after{content:"";display:inline-block;width:150px;height:2px;background:var(--navy);vertical-align:middle;margin:0 30px}
.join-title{top:920px}
.plan{position:absolute;background:var(--card);text-align:center;padding-top:44px}
.plan-basic{left:196px;top:1100px;width:388px;height:420px}
.plan-pro{left:612px;top:1048px;width:392px;height:492px;box-shadow:0 6px 18px rgba(0,0,0,.08)}
.plan-name{font-family:"Fredoka",Arial,sans-serif;font-weight:600;font-size:24px;color:var(--navy)}
.price{font-family:"Fredoka",Arial,sans-serif;font-weight:700;font-size:44px;color:var(--red);margin-top:22px;line-height:1}
.price.old{text-decoration:line-through;font-size:38px}
.per{font-size:12px;color:#9aa3ad;margin-top:4px}
.now{font-family:"Fredoka",Arial,sans-serif;font-weight:700;font-size:32px;color:var(--cyan);margin-top:6px}
.now small{font-size:16px;color:#9aa3ad;font-weight:500}
.features{list-style:none;text-align:left;margin:36px 0 0 40px}
.features li{display:flex;align-items:center;gap:16px;font-size:15px;height:42px;color:var(--text)}
.features svg{flex:0 0 18px}
.plan-btn{position:absolute;top:1548px;width:184px;height:46px;line-height:46px;font-size:14px}

/* Winners */
.winners{position:absolute;left:0;top:1660px;width:1200px;height:780px;background:var(--grey-bg)}
.winners-title{top:1756px}
.winner-photo{position:absolute;top:1900px;height:260px;border-radius:2px}
.winner{position:absolute;top:2200px;width:320px;text-align:center}
.winner h3{font-family:"Fredoka",Arial,sans-serif;font-weight:600;font-size:30px;color:var(--navy)}
.winner h3 span{color:var(--yellow-deep)}
.winner .prize{font-weight:700;font-size:15px;letter-spacing:1px;color:var(--navy);margin-top:6px}
.winner p{font-size:17px;font-weight:600;color:var(--navy);margin-top:6px}
.winner p b{color:var(--cyan);text-transform:uppercase}

/* Footer */
.footer{position:absolute;left:0;top:2440px;width:1200px;height:192px;background:var(--footer);color:var(--white);text-align:center}
.footer h4{margin-top:42px;font-size:16px;letter-spacing:3px;font-weight:700}
.footer h4::before,.footer h4::after{content:"";display:inline-block;width:60px;height:2px;background:var(--white);vertical-align:middle;margin:0 18px}
.footer a{display:block;margin-top:26px;font-size:17px;font-weight:600;color:var(--white);text-decoration:none}
</style>
</head>
<body>

<header class="hero">
  <div class="brand"><span class="brand-dot"></span><span class="brand-name">Starlit Getaways</span></div>
  <div class="island-art" role="img" aria-label="Illustration of white palm trees on a small island with clouds"></div>
  <span class="rule" style="left:262px"></span><span class="rule" style="left:798px"></span>
  <h1 class="headline">
    <span class="l1">Join &amp; Win</span>
    <span class="l2">A Holiday</span>
    <span class="l3">In <b>Rome</b></span>
    <span class="l4">For People</span>
  </h1>
  <form class="signup">
    <span class="field">Email</span>
    <span class="field">first name</span>
    <span class="field">Last name</span>
    <span class="field select">Which service ?</span>
    <div class="consent"><span class="box"></span><span>By entering your email address you agree to receive updates about the competition and our newsletter too</span></div>
    <span class="btn">Enter now</span>
  </form>
</header>

<h2 class="section-title join-title">Join Now</h2>

<section class="plan plan-basic">
  <div class="plan-name">1 Entry</div>
  <div class="price">£2.99</div>
  <div class="per">per month</div>
  <ul class="features">
    <li><svg width="18" height="18" viewBox="0 0 18 18"><path d="M3 3L15 15M15 3L3 15" stroke="#ef5b4b" stroke-width="2.5" stroke-linecap="round"/></svg>Weekly Deal Email</li>
    <li><svg width="18" height="18" viewBox="0 0 18 18"><path d="M2 9L7 14L16 4" fill="none" stroke="#2fb8a6" stroke-width="2.5" stroke-linecap="round"/></svg>Save £100's on Holidays</li>
    <li><svg width="18" height="18" viewBox="0 0 18 18"><path d="M2 9L7 14L16 4" fill="none" stroke="#2fb8a6" stroke-width="2.5" stroke-linecap="round"/></svg>Monthly Magazine</li>
    <li><svg width="18" height="18" viewBox="0 0 18 18"><path d="M2 9L7 14L16 4" fill="none" stroke="#2fb8a6" stroke-width="2.5" stroke-linecap="round"/></svg>1 Entries Every Month</li>
  </ul>
</section>

<section class="plan plan-pro">
  <div class="plan-name">15 Entries &amp; weekly deals</div>
  <div class="price old">£6.00</div>
  <div class="per">per month</div>
  <div class="now"><small>now</small> £4.99</div>
  <ul class="features">
    <li><svg width="18" height="18" viewBox="0 0 18 18"><path d="M2 9L7 14L16 4" fill="none" stroke="#2fb8a6" stroke-width="2.5" stroke-linecap="round"/></svg>Weekly Deal Email</li>
    <li><svg width="18" height="18" viewBox="0 0 18 18"><path d="M2 9L7 14L16 4" fill="none" stroke="#2fb8a6" stroke-width="2.5" stroke-linecap="round"/></svg>Save £100's on Holidays</li>
    <li><svg width="18" height="18" viewBox="0 0 18 18"><path d="M2 9L7 14L16 4" fill="none" stroke="#2fb8a6" stroke-width="2.5" stroke-linecap="round"/></svg>Monthly Magazine</li>
    <li><svg width="18" height="18" viewBox="0 0 18 18"><path d="M2 9L7 14L16 4" fill="none" stroke="#2fb8a6" stroke-width="2.5" stroke-linecap="round"/></svg>15 Entries Every Month</li>
  </ul>
</section>

<span class="btn plan-btn" style="left:298px">Go to Check Out</span>
<span class="btn plan-btn" style="left:716px">Go to Check Out</span>

<section class="winners"></section>
<h2 class="section-title winners-title">Previous Winners</h2>

<div class="winner-photo" style="left:112px;width:310px;background:linear-gradient(135deg,#8a8f99,#4a4440)" role="img" aria-label="Photo of April's winner on holiday in a city square"></div>
<div class="winner-photo" style="left:444px;width:318px;background:linear-gradient(135deg,#9a8a74,#5c4d3e)" role="img" aria-label="Photo of February's winner in front of a stone building"></div>
<div class="winner-photo" style="left:774px;width:316px;background:linear-gradient(135deg,#8c6c88,#3e3450)" role="img" aria-label="Photo of December's winner on a night out"></div>

<div class="winner" style="left:106px"><h3>April's <span>Winner</span></h3><div class="prize">PRIZE</div><p>A Week in <b>Portugal</b></p></div>
<div class="winner" style="left:442px"><h3>February's <span>Winner</span></h3><div class="prize">PRIZE</div><p>Flights to <b>New York City</b></p></div>
<div class="winner" style="left:772px"><h3>December's <span>Winner</span></h3><div class="prize">PRIZE</div><p>A Week in <b>Spain</b></p></div>

<footer class="footer">
  <h4>CONTACT</h4>
  <a href="mailto:hello@starlitgetaways.com">hello@starlitgetaways.com</a>
</footer>

</body>
</html>
```